Business Card Design

5* Hotel Property based on an island in Greece

My position is aparta from being a director, i'm on the accounts payable too, not sure how this should be stated, with a comma or "/"?

Sorry about the uploaded logo, it was a mistaken one!

There's also need to be added this  www.corvanteholdings.com on the back side of the card!

Also need to have the logo of the corvante holdings which can be found in a second on the brief! Thank you guys, irini

Industry/Entity Type

Business

Contact Information for Business Card

VERISTOKA PELLA Hotel
Irini Dravetsou
Director, AP Dept.

www.veristoka.gr
Peltira Island 85300
Greece

irinidravetsou@fenmail.com
+306951273064

```html
<!DOCTYPE html>
<html lang="en">
<head>
<meta charset="utf-8">
<title>Veristoka Pella Hotel – Business Card</title>
<link href="https://fonts.googleapis.com/css2?family=Quicksand:wght@300;400;500&display=swap" rel="stylesheet">
<style>
  :root {
    --board-bg: #f1f1f1;
    --card-bg: #ffffff;
    --ink: #3a3a3a;
    --ink-soft: #555555;
    --sea: #2a8fd6;
    --sea-light: #7fd0f3;
    --band: #86d1f2;
    --leaf: #8cc63f;
    --holding: #1d4f91;
    --label: #a9a9a9;
  }
  * { margin: 0; padding: 0; box-sizing: border-box; }
  html, body { width: 1200px; height: 848px; overflow: hidden; }
  body {
    position: relative;
    background: radial-gradient(ellipse at 40% 35%, #fbfbfb 0%, var(--board-bg) 70%, #e6e6e6 100%);
    font-family: "Quicksand", sans-serif;
    color: var(--ink);
  }

  /* Brand lockup */
  .brand { position: absolute; display: flex; align-items: center; }
  .brand-dot { border-radius: 50%; background: var(--sea-light); flex: none; }
  .brand-name { color: var(--ink); font-weight: 400; line-height: 1.05; }
  .brand-name span { display: block; }

  .brand--hero { left: 105px; top: 128px; }
  .brand--hero .brand-dot { width: 118px; height: 118px; margin-right: 24px; }
  .brand--hero .brand-name { font-size: 39px; }
  .brand--hero .brand-sub { font-size: 22px; letter-spacing: 8px; margin-top: 6px; }

  /* Cards */
  .card {
    position: absolute; left: 718px; width: 436px; height: 286px;
    background: var(--card-bg);
    box-shadow: 3px 5px 8px rgba(0,0,0,0.22);
  }
  .card--front { top: 70px; }
  .card--back { top: 465px; }

  .band {
    position: absolute; left: 0; right: 0; height: 25px;
    background: var(--band);
    color: #fff; font-size: 12px; font-weight: 500;
    letter-spacing: 4.6px; text-align: center; line-height: 25px;
  }
  .card--front .band { top: 245px; }
  .card--back .band { top: 246px; }

  .card--front .brand { left: 18px; top: 26px; }
  .card--front .brand-dot { width: 36px; height: 36px; margin-right: 10px; }
  .card--front .brand-name { font-size: 13.5px; }
  .card--front .brand-sub { font-size: 9px; letter-spacing: 3px; margin-top: 1px; }

  .holder { position: absolute; right: 28px; top: 106px; text-align: right; }
  .holder-name { font-size: 19px; font-weight: 400; color: var(--ink); }
  .holder-role { font-size: 13px; color: var(--sea); margin-top: 2px; }

  .contacts { position: absolute; left: 18px; top: 185px; list-style: none; }
  .contacts li { display: flex; align-items: center; height: 19px; font-size: 11.5px; color: var(--ink-soft); }
  .contacts svg { width: 14px; height: 14px; margin-right: 6px; flex: none; }

  .card--back .brand { left: 106px; top: 85px; }
  .card--back .brand-dot { width: 70px; height: 70px; margin-right: 12px; }
  .card--back .brand-name { font-size: 20px; }
  .card--back .brand-sub { font-size: 12.5px; letter-spacing: 4.5px; margin-top: 3px; }

  .holding { position: absolute; left: 9px; top: 222px; display: flex; align-items: center; }
  .holding-mark { width: 18px; height: 18px; background: var(--holding); margin-right: 5px; }
  .holding-name { font-size: 10px; color: var(--holding); font-weight: 500; }

  .side-label {
    position: absolute; left: 718px; width: 436px; text-align: center;
    font-size: 36px; font-weight: 300; color: var(--label);
  }
  .side-label--front { top: 380px; }
  .side-label--back { top: 770px; }
</style>
</head>
<body>

  <div class="brand brand--hero">
    <div class="brand-dot"></div>
    <div class="brand-name"><span>VERISTOKA PELLA</span><span class="brand-sub">HOTEL</span></div>
  </div>

  <section class="card card--front">
    <div class="brand">
      <div class="brand-dot"></div>
      <div class="brand-name"><span>VERISTOKA PELLA</span><span class="brand-sub">HOTEL</span></div>
    </div>

    <div class="holder">
      <p class="holder-name">Irini Dravetsou</p>
      <p class="holder-role">Director, AP Dept.</p>
    </div>

    <ul class="contacts">
      <li>
        <svg viewBox="0 0 14 14" aria-hidden="true"><rect width="14" height="14" rx="3" fill="var(--leaf)"/><circle cx="7" cy="7" r="4.2" fill="none" stroke="#fff" stroke-width="1"/><path d="M2.8 7h8.4M7 2.8c-1.8 2.3-1.8 6.1 0 8.4M7 2.8c1.8 2.3 1.8 6.1 0 8.4" fill="none" stroke="#fff" stroke-width="0.9"/></svg>
        Peltira Island 85300 Greece
      </li>
      <li>
        <svg viewBox="0 0 14 14" aria-hidden="true"><rect width="14" height="14" rx="3" fill="var(--leaf)"/><text x="7" y="10.3" text-anchor="middle" font-size="10" font-family="Quicksand, sans-serif" font-weight="500" fill="#fff">@</text></svg>
        irinidravetsou@fenmail.com
      </li>
      <li>
        <svg viewBox="0 0 14 14" aria-hidden="true"><rect width="14" height="14" rx="3" fill="var(--leaf)"/><path d="M4.2 3.2l1.6-.4 1 2.2-1 .8c.5 1.2 1.3 2 2.4 2.5l.8-1 2.2 1-.4 1.6c-3.6.3-6.8-2.9-6.6-6.7z" fill="#fff"/></svg>
        +306951273064
      </li>
    </ul>

    <div class="band">www.veristoka.gr</div>
  </section>
  <p class="side-label side-label--front">front</p>

  <section class="card card--back">
    <div class="brand">
      <div class="brand-dot"></div>
      <div class="brand-name"><span>VERISTOKA PELLA</span><span class="brand-sub">HOTEL</span></div>
    </div>

    <div class="holding">
      <div class="holding-mark"></div>
      <span class="holding-name">corvante holdings</span>
    </div>

    <div class="band">www.corvanteholdings.com</div>
  </section>
  <p class="side-label side-label--back">back</p>

</body>
</html>
```